Gulf Book About Father - need cover design named - الوهج

The book talks about the good father who teaches his sons high principles and values, to be successful people in their lives.

Book size - 15 cm high
21 cm width
Data on the cover:
Name of the Book: الوهج
Author: دكتور/ وضاح بن ناصر القرملي- Just write the name without the word writer
1440-2018
Logo of the Publishing House

Target Market(s)

Book submitted to children - Families - Schools - Public libraries

Requirements
Must have
• Design must include one or all of these options:
• The first option: a picture that has a meaning for a father who has values and principles with the son or children, expresses the contradiction - education, etc. -
• The background is to express the tender love or taken from the Emirates flag
• The second option: abstract art - with a background taken from the colors of the flag of the Emirates - or colors about love and tenderness
Should not have
• direct image

```html
<!DOCTYPE html>
<html lang="ar" dir="rtl">
<head>
<meta charset="utf-8">
<title>الوهج — غلاف كتاب</title>
<link rel="stylesheet" href="https://fonts.googleapis.com/css2?family=Cairo:wght@300;400&family=Reem+Kufi:wght@400&display=swap">
<style>
  :root {
    --sky-top: #e9a27e;
    --sky-mid: #f1bc97;
    --sky-glow: #fbe6c4;
    --sun: #fff6dc;
    --cloud-warm: #e7a153;
    --ground-dark: #5a2a14;
    --flag-red: #c9362b;
    --flag-white: #ffffff;
    --flag-green: #1e7a2c;
    --author-ink: #8a2419;
    --publisher-ink: #b3261e;
  }
  * { margin: 0; padding: 0; box-sizing: border-box; }
  html, body { width: 800px; height: 1200px; overflow: hidden; }
  body { background: var(--sky-top); }
  .cover {
    position: relative;
    width: 800px;
    height: 1200px;
    overflow: hidden;
  }
  .cover-scene {
    position: absolute;
    inset: 0;
    background:
      radial-gradient(ellipse 260px 200px at 400px 760px, var(--sun) 0%, var(--sky-glow) 35%, rgba(251,230,196,0) 100%),
      radial-gradient(ellipse 600px 260px at 380px 980px, rgba(231,161,83,0.85) 0%, rgba(231,161,83,0) 100%),
      linear-gradient(180deg, var(--sky-top) 0%, var(--sky-mid) 45%, var(--sky-glow) 62%, var(--cloud-warm) 82%, var(--ground-dark) 100%);
  }
  .book-title {
    position: absolute;
    top: 110px;
    left: 90px;
    width: 640px;
    text-align: center;
    font-family: "Cairo", sans-serif;
    font-weight: 300;
    font-size: 200px;
    line-height: 1;
    white-space: nowrap;
  }
  .title-green { color: var(--flag-green); }
  .title-white { color: var(--flag-white); }
  .title-red { color: var(--flag-red); }
  .author {
    position: absolute;
    top: 478px;
    left: 110px;
    width: 560px;
    text-align: center;
    font-family: "Reem Kufi", sans-serif;
    font-size: 36px;
    color: var(--author-ink);
    white-space: nowrap;
  }
  .edition-year {
    position: absolute;
    top: 540px;
    left: 110px;
    width: 560px;
    text-align: center;
    font-family: "Reem Kufi", sans-serif;
    font-size: 24px;
    color: var(--author-ink);
    direction: ltr;
  }
  .publisher {
    position: absolute;
    left: 52px;
    bottom: 40px;
    display: flex;
    flex-direction: column;
    align-items: center;
    gap: 8px;
  }
  .publisher-mark {
    width: 70px;
    height: 70px;
    background: var(--publisher-ink);
  }
  .publisher-name {
    font-family: "Reem Kufi", sans-serif;
    font-size: 22px;
    color: var(--publisher-ink);
  }
</style>
</head>
<body>
  <main class="cover">
    <div class="cover-scene" role="img" aria-label="صورة ظلية لأب يحمل طفله على كتفيه والطفل يفتح ذراعيه أمام سماء الغروب الدافئة"></div>
    <h1 class="book-title"><span class="title-green">ال</span><span class="title-white">وه</span><span class="title-red">ج</span></h1>
    <p class="author">دكتور/ وضاح بن ناصر القرملي</p>
    <p class="edition-year">1440 - 2018</p>
    <div class="publisher">
      <div class="publisher-mark"></div>
      <span class="publisher-name">دار الندى</span>
    </div>
  </main>
</body>
</html>
```